Business Card Design for Kestrelwood Carpentry

I need a business card design for my carpentry company Kestrelwood Carpentry. Ive attached files with all information I require on both sides. Look forward to seeing your design.

```html
<!DOCTYPE html>
<html lang="en">
<head>
<meta charset="utf-8">
<title>Kestrelwood Carpentry – Business Card</title>
<link href="https://fonts.googleapis.com/css2?family=Oswald:wght@500;700&family=Open+Sans:wght@600&display=swap" rel="stylesheet">
<style>
  :root {
    --orange: #ef5a24;
    --orange-light: #f26a30;
    --ink: #1c1a1a;
    --paper: #ffffff;
    --backdrop: #e9e7e4;
  }
  * { box-sizing: border-box; margin: 0; padding: 0; }
  html, body { width: 1200px; height: 900px; overflow: hidden; }
  body { background: var(--backdrop); position: relative; font-family: "Open Sans", sans-serif; }

  .card {
    position: absolute;
    width: 600px; height: 343px;
    border-radius: 18px;
    overflow: hidden;
    box-shadow: 0 10px 30px rgba(0,0,0,.18);
  }
  .card-front { left: 80px; top: 80px; background: var(--paper); }
  .card-back { left: 520px; top: 477px; background: linear-gradient(135deg, var(--orange-light), var(--orange)); color: var(--paper); }

  .brand {
    position: absolute; left: 0; right: 0;
    display: flex; align-items: center; justify-content: center; gap: 14px;
  }
  .brand-name {
    font-family: "Oswald", sans-serif; font-weight: 700;
    font-size: 40px; letter-spacing: 2px; text-transform: uppercase; line-height: 1;
  }
  .brand-dot { width: 16px; height: 16px; border-radius: 50%; }
  .brand-rule { position: absolute; left: 150px; right: 150px; height: 3px; }

  .card-front .brand { top: 78px; }
  .card-front .brand-name { color: var(--ink); }
  .card-front .brand-dot { background: var(--orange); }
  .card-front .brand-rule { top: 138px; background: var(--orange); }

  .phone {
    position: absolute; top: 168px; left: 0; right: 0;
    display: flex; justify-content: center; align-items: center; gap: 12px;
    font-family: "Oswald", sans-serif; font-weight: 500; font-size: 22px; color: var(--ink);
  }
  .tagline {
    position: absolute; top: 222px; left: 0; right: 0; text-align: center;
    font-family: "Oswald", sans-serif; font-weight: 500; font-size: 26px;
    color: var(--orange); text-transform: uppercase; letter-spacing: .5px;
  }
  .tagline .quote { color: var(--ink); }
  .front-band { position: absolute; left: 0; right: 0; bottom: 0; height: 24px; background: var(--orange); border-top: 4px solid var(--ink); }

  .card-back .brand { top: 58px; }
  .card-back .brand-name { color: var(--paper); }
  .card-back .brand-dot { background: var(--paper); }
  .card-back .brand-rule { top: 118px; background: var(--paper); }

  .services {
    position: absolute; top: 150px; left: 30px; right: 30px;
    text-align: center; font-size: 14px; line-height: 1.9; font-weight: 600;
  }
  .services .sep { margin: 0 6px; }
  .contact {
    position: absolute; top: 248px; left: 0; right: 0; text-align: center;
    font-size: 14px; font-weight: 600; line-height: 1.7;
  }
  .contact-rule { display: inline-block; width: 80px; height: 2px; background: var(--paper); vertical-align: middle; margin: 0 12px; }
</style>
</head>
<body>
  <section class="card card-front" aria-label="Card front">
    <div class="brand"><span class="brand-dot"></span><span class="brand-name">Kestrelwood Carpentry</span><span class="brand-dot"></span></div>
    <div class="brand-rule"></div>
    <div class="phone">
      <svg width="22" height="18" viewBox="0 0 22 18" aria-hidden="true"><path d="M2 6c0-3 4-4 9-4s9 1 9 4v2h-5V6H7v2H2z M5 10h12l2 7H3z" fill="#ef5a24"/><circle cx="11" cy="13.5" r="2" fill="#fff"/></svg>
      <span>0400 555 183</span>
    </div>
    <p class="tagline"><span class="quote">“</span>Anything carpentry. Anywhere in Sydney<span class="quote">”</span></p>
    <div class="front-band"></div>
  </section>

  <section class="card card-back" aria-label="Card back">
    <div class="brand"><span class="brand-dot"></span><span class="brand-name">Kestrelwood Carpentry</span><span class="brand-dot"></span></div>
    <div class="brand-rule"></div>
    <p class="services">
      Desk &amp; Pergola<span class="sep">•</span>Shop Fitouts<span class="sep">•</span>Wall &amp; Roof Framing<span class="sep">•</span>Refurbishment<br>
      Door &amp; Windows<span class="sep">•</span>Fences/Gates<span class="sep">•</span>Attic Conversions<span class="sep">•</span>Privacy Screens<br>
      Timber Flooring<span class="sep">•</span>Wall Cladding<span class="sep">•</span>Extension &amp; More...
    </p>
    <p class="contact">
      <span class="contact-rule"></span>LIC # 4810357K<span class="contact-rule"></span><br>
      kestrelwoodcarpentry@mail.com
    </p>
  </section>
</body>
</html>
```